Infectious Diseases Research Laboratory Needs Business Card

We need a business card for an academic research laboratory based in Kansas City called MORVEK. The full lab name is Microbial Dose-Response/Exposure Bridging Studies Laboratory, but this does not need to be incorporated. We study novel ways to optimize the treatment of multidrug-resistant bacterial infections ("superbugs") throughout the entire biomedical research spectrum (from benchtop to bedside). The name MORVEK is not only an acronym for our lab name, but also represents our desire to make discoveries and explore the unknown (the stars, if you well). It also serves as an ode to the state of Kansas motto where we are based, ad astra per aspera ("to the stars, through difficulty").

Target Market(s)

Pharmaceutical companies, researchers

Industry/Entity Type

Pharmaceutical

Contact Information for Business Card

The business card should incorporate and complement our new logo (see uploaded files). Double-sided designs are preferred. Looking for something modern, but professional.

Font styles to use
Sans Serif

Requirements
Must have
• Double-sided. One side would ideally be a solid color incorporating logo and the other should also have the logo (smaller), but incorporate staff information.
• Color codes:
• Red: #F04C51
• Blue: #3477B5
• Gray: #808285

```html
<!DOCTYPE html>
<html lang="en">
<head>
<meta charset="utf-8">
<title>MORVEK Business Card</title>
<link href="https://fonts.googleapis.com/css2?family=Lato:wght@300;400;700&display=swap" rel="stylesheet">
<style>
  :root {
    --red: #F04C51;
    --blue: #3477B5;
    --band-blue: #1E75B0;
    --gray: #808285;
    --ink: #2b2b2b;
    --card-light: #f1f1f1;
    --card-dark: #232323;
    --emboss: #2e2e2e;
    --stage: #d9d9d9;
  }
  * { margin: 0; padding: 0; box-sizing: border-box; }
  html, body { width: 1200px; height: 716px; overflow: hidden; }
  body {
    background: var(--stage);
    font-family: "Lato", sans-serif;
    position: relative;
  }
  .card {
    position: absolute;
    top: 203px;
    width: 540px;
    height: 309px;
    border-radius: 22px;
    overflow: hidden;
  }

  /* ---------- back side ---------- */
  .card-back {
    left: 40px;
    background: var(--card-dark);
  }
  .back-brand {
    position: absolute;
    left: 0; right: 0; top: 96px;
    text-align: center;
  }
  .back-wordmark {
    display: inline-flex;
    align-items: center;
    gap: 16px;
  }
  .back-wordmark .mark-dot {
    width: 34px; height: 34px; border-radius: 50%;
    background: var(--emboss);
    box-shadow: inset 1px 1px 2px #111, inset -1px -1px 1px #3a3a3a;
  }
  .back-wordmark .name {
    font-weight: 300;
    font-size: 70px;
    letter-spacing: 8px;
    color: var(--emboss);
    text-shadow: -1px -1px 1px #111, 1px 1px 1px #3c3c3c;
  }
  .back-lab {
    margin: 10px auto 0;
    width: 330px;
    border-top: 1px solid #333;
    padding-top: 6px;
    font-size: 10px;
    letter-spacing: 1.6px;
    line-height: 1.5;
    text-transform: uppercase;
    color: #333;
    text-shadow: 1px 1px 0 #3a3a3a;
  }

  /* ---------- front side ---------- */
  .card-front {
    left: 620px;
    background: var(--card-light);
  }
  .identity {
    position: absolute;
    left: 30px; top: 34px;
    padding-left: 12px;
    border-left: 6px solid var(--red);
  }
  .identity .person {
    font-size: 26px;
    line-height: 1;
    color: var(--ink);
    font-weight: 300;
  }
  .identity .person strong { font-weight: 700; }
  .identity .role {
    font-size: 15px;
    color: var(--red);
    margin-top: 3px;
  }
  .rule-blue {
    position: absolute;
    left: 0; top: 104px;
    width: 320px; height: 2px;
    background: var(--blue);
  }
  .rule-red {
    position: absolute;
    left: 320px; right: 0; top: 156px;
    height: 2px;
    background: var(--red);
  }
  .bubble-field {
    position: absolute;
    right: 0; top: 60px;
    width: 230px; height: 180px;
    background: radial-gradient(ellipse at 55% 55%, rgba(180,180,180,0.35), rgba(241,241,241,0) 70%);
  }
  .front-brand {
    position: absolute;
    right: 30px; top: 114px;
    display: flex; align-items: center; gap: 10px;
  }
  .front-brand .mark-dot {
    width: 26px; height: 26px; border-radius: 50%;
    background: var(--blue);
  }
  .front-brand .name {
    font-weight: 300;
    font-size: 38px;
    letter-spacing: 3px;
    color: var(--red);
  }
  .contacts {
    position: absolute;
    left: 30px; top: 132px;
    list-style: none;
  }
  .contacts li {
    display: flex; align-items: center; gap: 12px;
    height: 30px;
    font-size: 14px;
    color: #444;
  }
  .contacts .icon {
    width: 22px; height: 22px;
    border: 1.5px solid var(--blue);
    border-radius: 50%;
    display: flex; align-items: center; justify-content: center;
  }
  .band {
    position: absolute;
    left: 0; right: 0; bottom: 0;
    height: 56px;
    background: var(--band-blue);
    display: flex; align-items: center; justify-content: space-between;
    padding: 0 30px;
  }
  .band .site {
    color: #fff;
    font-size: 17px;
    letter-spacing: 0.3px;
  }
  .social { display: flex; gap: 12px; }
  .social span {
    width: 16px; height: 16px;
    border-radius: 3px;
    background: #e8eef5;
  }
</style>
</head>
<body>

<section class="card card-back" aria-label="Card back">
  <div class="back-brand">
    <div class="back-wordmark">
      <span class="mark-dot"></span>
      <span class="name">MORVEK</span>
    </div>
    <p class="back-lab">Microbial Dose-Response/Exposure<br>Bridging Studies Laboratory</p>
  </div>
</section>

<section class="card card-front" aria-label="Card front">
  <div class="identity">
    <p class="person">Your <strong>Name</strong></p>
    <p class="role">Field Service Engineer</p>
  </div>
  <div class="rule-blue"></div>
  <div class="rule-red"></div>
  <div class="bubble-field" role="img" aria-label="Soft gray bubble pattern behind the logo"></div>
  <div class="front-brand">
    <span class="mark-dot"></span>
    <span class="name">MORVEK</span>
  </div>

  <ul class="contacts">
    <li>
      <span class="icon">
        <svg width="12" height="12" viewBox="0 0 24 24"><path fill="#F04C51" d="M6.6 10.8a15.1 15.1 0 0 0 6.6 6.6l2.2-2.2a1 1 0 0 1 1-.25 11.4 11.4 0 0 0 3.6.57 1 1 0 0 1 1 1V20a1 1 0 0 1-1 1A17 17 0 0 1 3 4a1 1 0 0 1 1-1h3.5a1 1 0 0 1 1 1c0 1.25.2 2.45.57 3.57a1 1 0 0 1-.25 1z"/></svg>
      </span>
      000 000 0000
    </li>
    <li>
      <span class="icon">
        <svg width="10" height="13" viewBox="0 0 10 16"><rect x="0.5" y="0.5" width="9" height="15" rx="1.5" fill="#F04C51"/><rect x="2" y="2.5" width="6" height="8" fill="#fff"/><circle cx="5" cy="13" r="1" fill="#fff"/></svg>
      </span>
      000 000 0000
    </li>
    <li>
      <span class="icon">
        <svg width="12" height="9" viewBox="0 0 16 12"><rect width="16" height="12" rx="1" fill="#F04C51"/><path d="M1 1l7 6 7-6" stroke="#fff" stroke-width="1.4" fill="none"/></svg>
      </span>
      dana.whitfield@prairiebenchlab.net
    </li>
  </ul>

  <div class="band">
    <span class="site">www.yourwebsite.com</span>
    <div class="social" aria-label="Social profiles">
      <span></span><span></span><span></span>
    </div>
  </div>
</section>

</body>
</html>
```